Business Card Design

Please use the Logo for colors and styles, and create a business card using the following info:

Matthias Lorbeer
Web Developer

Lorbeer Systems
+41 76 418 57 90
matthias@lorbeer-systems.ch
www.lorbeer-systems.ch

Download the logo at http://lorbeer-systems.ch/tl_files/lorbeer_systems.zip

Thanks for your works!

```html
<!DOCTYPE html>
<html lang="en">
<head>
<meta charset="utf-8">
<title>Lorbeer Systems – Business Card</title>
<link rel="stylesheet" href="https://fonts.googleapis.com/css2?family=Questrial&display=swap">
<style>
  :root {
    --navy: #0e4470;
    --brand-blue: #0b7fd0;
    --soft-blue: #3f9be0;
    --white: #ffffff;
    --stage: #e6e9ed;
    --logo-ink: #0c5a96;
  }
  * { margin: 0; padding: 0; box-sizing: border-box; }
  html, body { width: 1200px; height: 821px; overflow: hidden; }
  body {
    background: var(--stage);
    font-family: "Questrial", "Century Gothic", sans-serif;
    position: relative;
  }
  .card {
    position: absolute;
    top: 260px;
    width: 540px;
    height: 300px;
    border-radius: 12px;
    overflow: hidden;
    box-shadow: 0 6px 18px rgba(0, 0, 0, 0.18);
  }
  .card--front { left: 40px; background: var(--white); }
  .card--back { left: 620px; background: var(--navy); }

  .card__band {
    position: absolute;
    left: 0; right: 0; top: 130px; bottom: 0;
    background: var(--navy);
  }

  .wordmark {
    position: absolute;
    font-size: 36px;
    letter-spacing: -0.5px;
    line-height: 1;
    white-space: nowrap;
  }
  .card--front .wordmark { left: 28px; top: 46px; color: var(--logo-ink); }
  .card--back .wordmark {
    left: 0; right: 0; top: 114px; text-align: center;
    font-size: 44px; color: var(--white);
  }

  .holder { position: absolute; left: 28px; top: 150px; color: var(--white); }
  .holder__name { font-size: 23px; line-height: 1.1; }
  .holder__role { font-size: 12px; opacity: 0.85; margin-top: 2px; }
  .holder-accent {
    position: absolute; left: 0; top: 156px;
    width: 6px; height: 34px; background: var(--brand-blue);
    border-radius: 0 3px 3px 0;
  }

  .contact {
    position: absolute; left: 290px; top: 200px;
    color: var(--white); font-size: 14px; line-height: 19px;
  }
  .contact__company { font-size: 15px; }

  .site-url {
    position: absolute; left: 0; right: 0; bottom: 30px;
    text-align: center; font-size: 16px; color: var(--white);
  }
  .site-url__muted { color: var(--soft-blue); }
</style>
</head>
<body>
  <section class="card card--front" aria-label="Business card front">
    <div class="card__band"></div>
    <div class="wordmark">LORBEER SYSTEMS</div>
    <span class="holder-accent"></span>
    <div class="holder">
      <p class="holder__name">Matthias Lorbeer</p>
      <p class="holder__role">Web Developer</p>
    </div>
    <div class="contact">
      <p class="contact__company">Lorbeer Systems</p>
      <p>P: +41 76 418 57 90</p>
      <p>E: matthias@lorbeer-systems.ch</p>
      <p>www.lorbeer-systems.ch</p>
    </div>
  </section>

  <section class="card card--back" aria-label="Business card back">
    <div class="wordmark">LORBEER SYSTEMS</div>
    <p class="site-url"><span class="site-url__muted">www.</span>lorbeer-systems<span class="site-url__muted">.ch</span></p>
  </section>
</body>
</html>
```